Economics of an Assumption vs Obtaining a New Loan at Current Market Rate

I need to marketing flyer that has fields that calculate mortgage payments amongst other calculations. I have a rough draft that I will attach.

The idea is to provide a tool for a real estate agent to use to illustrate to a potential buyer what a payment would be if they assumed the existing loan on the house or took out a new loan at current market.

The flyer needs to be able to allow an agent to drop in their logo, photo, and contact along with the loan officers photo and contact info.

You can google open house flyer to see examples of what the overall artwork and presentation can look like.

Target Market(s)

Home Buyers

Industry/Entity Type

Real Estate

Colors
F0912C
F2A743
F7CA91
FBE8D2
FDF5EE
EE7325
F08F49
F5BC92
FAE3D3
FDF4ED

Requirements
Must have
• A way to calculate mortgage payment
Nice to have
• Photo and logo drop ins

```html
<!DOCTYPE html>
<html lang="en">
<head>
<meta charset="utf-8">
<title>Ravelmoor – Assumption vs New Loan Flyer</title>
<link href="https://fonts.googleapis.com/css2?family=Source+Sans+3:ital,wght@0,400;0,500;0,600;0,700;1,400&display=swap" rel="stylesheet">
<style>
  :root{
    --orange:#F0912C;
    --orange-light:#F2A743;
    --orange-deep:#EE7325;
    --cream:#FDF5EE;
    --ink:#111111;
    --white:#ffffff;
    --link:#1f5fa8;
  }
  *{box-sizing:border-box;margin:0;padding:0}
  html,body{width:856px;height:1200px;overflow:hidden;background:var(--white)}
  body{font-family:"Source Sans 3",sans-serif;color:var(--ink)}
  .flyer{position:relative;width:856px;height:1200px;overflow:hidden;background:var(--orange-light)}
  .abs{position:absolute}

  .hero-photo{left:0;top:0;width:856px;height:470px;
    background:linear-gradient(180deg,#6f7fa6 0%,#9aa3bd 22%,#b8987a 45%,#a9835e 62%,#8b7a68 82%,#b7aea3 100%)}
  .hero-shapes{left:0;top:0}

  .brand{left:110px;top:40px;height:64px;display:flex;align-items:center;gap:10px;
    font-size:42px;font-weight:400;color:var(--orange);letter-spacing:1px}
  .brand-dot{width:28px;height:28px;border-radius:50%;background:var(--orange)}

  .price-label{left:157px;top:510px;font-size:36px;font-weight:700;letter-spacing:.5px}
  .price-box{left:480px;top:510px;width:220px;height:42px;border:2px solid #222;border-radius:4px}

  .panels{left:0;top:565px}
  .section-pill{left:12px;top:572px;width:295px;height:42px;background:var(--white);
    border-radius:0 22px 22px 0;padding-left:14px;display:flex;align-items:center;
    font-size:23px;font-weight:700;letter-spacing:1.6px}
  .row-label{font-size:18px;font-weight:500;line-height:22px}
  .current .row-label{color:var(--white)}
  .colon{font-size:18px;font-weight:500;line-height:22px}
  .current .colon{color:var(--white)}
  .field{height:23px;font-size:12.5px;display:flex;align-items:center;padding-left:20px}
  .current .field{border:1.5px solid var(--white);color:var(--white)}
  .new .field{border:1.5px solid #222;background:var(--white);padding-left:15px;font-size:13px;font-weight:500}
  .new-title{left:412px;top:578px;font-size:22px;font-weight:700;letter-spacing:1.4px}
  .new .row-label{color:#222}
  .small-note{font-size:8px;line-height:7px;margin-left:8px;font-weight:500}

  .difference{left:0;top:835px;width:856px;height:105px;background:var(--orange-light)}
  .diff-label{left:130px;top:843px;font-size:34px;font-weight:700}
  .diff-box{left:540px;top:852px;width:191px;height:30px;border:1.5px solid #222;
    font-size:13.5px;display:flex;align-items:center;justify-content:center}
  .certified{left:0;top:882px;width:856px;text-align:center;font-size:35px;font-weight:700}

  .gallery-pill{left:0;top:952px;width:400px;height:50px;background:var(--cream);
    border-radius:0 25px 25px 0;padding-left:25px;display:flex;align-items:center;
    font-size:21px;font-style:italic;letter-spacing:2.4px}
  .thumb{top:1017px;width:104px;height:102px;border:4px solid var(--white);border-radius:14px;
    background:linear-gradient(180deg,#7a87aa 0%,#a9a6b3 30%,#b08a63 55%,#9a7a5c 78%,#b1a89d 100%)}
  .logo-card{left:304px;top:1017px;width:104px;height:102px;background:var(--white);border-radius:12px;
    display:flex;align-items:center;justify-content:center;gap:4px;font-size:16px;color:var(--orange)}
  .logo-card .brand-dot{width:11px;height:11px}
  .follow{left:95px;top:1128px;font-size:18px;color:var(--white);display:flex;align-items:center;gap:8px}
  .social{width:25px;height:25px;border:2px solid var(--white);border-radius:50%}

  .contact-pill{left:498px;top:955px;width:358px;height:48px;background:var(--orange);
    border-radius:24px 0 0 24px;padding-left:18px;display:flex;align-items:center;
    font-size:19px;font-weight:700;color:var(--white)}
  .contact-row{left:508px;display:flex;align-items:center;gap:14px;font-size:19px;color:var(--link)}
  .contact-row b{font-weight:700}
  .contact-icon{width:24px;height:24px}

  .footer-bar{left:0;top:1172px;width:856px;height:28px;background:var(--orange-deep)}
</style>
</head>
<body>
<main class="flyer">

  <div class="abs hero-photo" role="img" aria-label="Photo of the listed single-storey stucco home with tiled roof under a cloudy sky"></div>

  <svg class="abs hero-shapes" width="856" height="565" viewBox="0 0 856 565" aria-hidden="true">
    <defs>
      <linearGradient id="silver" x1="0" x2="1">
        <stop offset="0" stop-color="#8a8a8a"/><stop offset="0.5" stop-color="#e6e6e6"/><stop offset="1" stop-color="#8a8a8a"/>
      </linearGradient>
    </defs>
    <path d="M12 12 H490 C430 90 300 150 150 143 C90 140 40 128 12 115 Z" fill="var(--white)"/>
    <path d="M12 90 C40 120 90 138 150 143 C300 150 430 90 490 12 H530 C460 110 320 158 150 150 C80 146 30 125 12 105 Z" fill="url(#silver)" opacity=".85"/>
    <path d="M285 138 C390 120 470 70 530 12 H510 C455 70 385 112 285 138 Z" fill="var(--orange)"/>
    <path d="M0 425 C200 475 500 485 856 430 V445 C500 495 200 488 0 445 Z" fill="url(#silver)"/>
    <path d="M0 438 C200 486 500 492 856 444 V565 H0 Z" fill="var(--orange-light)"/>
    <path d="M0 436 C200 485 500 490 856 442 V452 C500 498 200 492 0 450 Z" fill="var(--white)"/>
  </svg>

  <div class="abs brand"><span class="brand-dot"></span>Ravelmoor</div>

  <div class="abs price-label">PURCHASE&nbsp; PRICE :</div>
  <div class="abs price-box"></div>

  <svg class="abs panels" width="856" height="270" viewBox="0 0 856 270" aria-hidden="true">
    <defs>
      <linearGradient id="greyPanel" x1="0" x2="1">
        <stop offset="0" stop-color="#bdbdbd"/><stop offset="0.12" stop-color="#ececec"/><stop offset="1" stop-color="#ffffff"/>
      </linearGradient>
    </defs>
    <rect x="0" y="0" width="856" height="270" fill="var(--orange)"/>
    <path d="M362 0 H856 V270 H408 C395 170 380 80 362 0 Z" fill="url(#greyPanel)"/>
  </svg>

  <section class="current">
    <div class="abs section-pill">CURRENT MORTGAGE :</div>
    <div class="abs row-label" style="left:27px;top:621px">Loan ammount</div>
    <div class="abs row-label" style="left:27px;top:648px">Interest rate</div>
    <div class="abs row-label" style="left:27px;top:675px">Principal 3 interest</div>
    <div class="abs row-label" style="left:27px;top:702px">Mortgage Insurance</div>
    <div class="abs row-label" style="left:27px;top:730px">Total</div>
    <div class="abs row-label" style="left:27px;top:757px">Years</div>
    <div class="abs row-label" style="left:154px;top:757px">Months</div>
    <div class="abs row-label" style="left:27px;top:787px">Delta</div>
    <div class="abs colon" style="left:225px;top:621px">:</div>
    <div class="abs colon" style="left:225px;top:648px">:</div>
    <div class="abs colon" style="left:225px;top:675px">:</div>
    <div class="abs colon" style="left:225px;top:702px">:</div>
    <div class="abs colon" style="left:225px;top:730px">:</div>
    <div class="abs field" style="left:243px;top:621px;width:115px">Allow Input</div>
    <div class="abs field" style="left:243px;top:648px;width:115px">Allow Input</div>
    <div class="abs field" style="left:243px;top:675px;width:115px">Allow Input</div>
    <div class="abs field" style="left:243px;top:702px;width:115px">Allow Input</div>
    <div class="abs field" style="left:243px;top:729px;width:115px"></div>
    <div class="abs field" style="left:88px;top:757px;width:58px"></div>
    <div class="abs field" style="left:242px;top:757px;width:59px"></div>
    <div class="abs field" style="left:88px;top:786px;width:268px;padding-left:18px">Purchase price minus lean amount</div>
  </section>

  <section class="new">
    <div class="abs new-title">New Mortgage 10% Down Payment</div>
    <div class="abs row-label" style="left:417px;top:628px">Loan ammount</div>
    <div class="abs row-label" style="left:417px;top:655px">Interest rate</div>
    <div class="abs row-label" style="left:417px;top:683px">Principal 3 interest</div>
    <div class="abs row-label" style="left:417px;top:710px">Mortgage Insurance</div>
    <div class="abs row-label" style="left:417px;top:737px">Total</div>
    <div class="abs row-label" style="left:417px;top:765px">Term</div>
    <div class="abs row-label" style="left:543px;top:765px">Years</div>
    <div class="abs row-label" style="left:417px;top:794px">Down payment amount</div>
    <div class="abs colon" style="left:614px;top:628px">:</div>
    <div class="abs colon" style="left:614px;top:655px">:</div>
    <div class="abs colon" style="left:614px;top:683px">:</div>
    <div class="abs colon" style="left:614px;top:710px">:</div>
    <div class="abs colon" style="left:614px;top:737px">:</div>
    <div class="abs field" style="left:632px;top:628px;width:195px">90% of purchase price</div>
    <div class="abs field" style="left:632px;top:655px;width:195px">Input</div>
    <div class="abs field" style="left:632px;top:682px;width:195px">Calc payment</div>
    <div class="abs field" style="left:632px;top:709px;width:195px">Input %</div>
    <div class="abs field" style="left:632px;top:736px;width:195px">Principal interest +<span class="small-note">Mortgage<br>Insurance</span></div>
    <div class="abs field" style="left:477px;top:764px;width:58px;padding-left:12px">Input</div>
    <div class="abs field" style="left:663px;top:793px;width:58px"></div>
  </section>

  <section class="abs difference"></section>
  <div class="abs diff-label">PAYMENT DIFFERENCE :</div>
  <div class="abs diff-box">Difference Between totals</div>
  <div class="abs certified">This property is “Keep This Rate Approved”</div>

  <svg class="abs" style="left:0;top:940px" width="856" height="232" viewBox="0 0 856 232" aria-hidden="true">
    <defs>
      <linearGradient id="greyBottom" x1="0" x2="1">
        <stop offset="0" stop-color="#bdbdbd"/><stop offset="0.15" stop-color="#ececec"/><stop offset="1" stop-color="#ffffff"/>
      </linearGradient>
    </defs>
    <rect width="856" height="232" fill="var(--orange)"/>
    <path d="M418 0 H856 V232 H408 Z" fill="url(#greyBottom)"/>
  </svg>

  <div class="abs gallery-pill">Picture New Mortgage</div>
  <div class="abs thumb" style="left:33px" role="img" aria-label="Photo of the home from the left side"></div>
  <div class="abs thumb" style="left:168px" role="img" aria-label="Photo of the home entrance"></div>
  <div class="abs logo-card"><span class="brand-dot"></span>Ravelmoor</div>
  <div class="abs follow">Follow us on : <span class="social"></span><span class="social"></span></div>

  <div class="abs contact-pill">For a FREE Quote Please Contact Us:</div>

  <div class="abs contact-row" style="top:1015px">
    <svg class="contact-icon" viewBox="0 0 24 24" aria-hidden="true"><circle cx="12" cy="12" r="11" fill="none" stroke="var(--link)" stroke-width="1.5"/><path d="M8 6.5c.6-.5 1.3-.4 1.6.2l1 2c.2.5.1 1-.3 1.3l-.7.6c.6 1.4 1.5 2.4 2.9 3.1l.6-.7c.3-.4.9-.5 1.3-.3l2 1c.6.3.7 1 .2 1.6l-.9.9c-.7.7-1.8.8-2.8.3-2.5-1.3-4.3-3.1-5.5-5.6-.4-1-.3-2 .4-2.7z" fill="var(--link)"/></svg>
    <span>OFFICE &nbsp;: <b>0123456789</b></span>
  </div>
  <div class="abs contact-row" style="top:1051px">
    <svg class="contact-icon" viewBox="0 0 24 24" aria-hidden="true"><circle cx="12" cy="12" r="11" fill="none" stroke="var(--link)" stroke-width="1.5"/><path d="M8 6.5c.6-.5 1.3-.4 1.6.2l1 2c.2.5.1 1-.3 1.3l-.7.6c.6 1.4 1.5 2.4 2.9 3.1l.6-.7c.3-.4.9-.5 1.3-.3l2 1c.6.3.7 1 .2 1.6l-.9.9c-.7.7-1.8.8-2.8.3-2.5-1.3-4.3-3.1-5.5-5.6-.4-1-.3-2 .4-2.7z" fill="var(--link)"/></svg>
    <span>MOBILE : <b>0123456789</b></span>
  </div>
  <div class="abs contact-row" style="top:1090px">
    <svg class="contact-icon" viewBox="0 0 24 24" aria-hidden="true"><circle cx="12" cy="12" r="11" fill="none" stroke="var(--link)" stroke-width="1.5"/><circle cx="12" cy="12" r="7" fill="none" stroke="var(--link)" stroke-width="1.3"/><path d="M5 12h14M12 5v14M12 5c-3 3.5-3 10.5 0 14M12 5c3 3.5 3 10.5 0 14" fill="none" stroke="var(--link)" stroke-width="1.1"/></svg>
    <span>www.<b>yourwebsite</b>.com</span>
  </div>
  <div class="abs contact-row" style="top:1128px">
    <svg class="contact-icon" viewBox="0 0 24 24" aria-hidden="true"><circle cx="12" cy="12" r="11" fill="none" stroke="var(--link)" stroke-width="1.5"/><path d="M6.5 10 12 6.5 17.5 10v6.5h-11z" fill="var(--link)"/><path d="M6.5 10 12 13.5 17.5 10" fill="none" stroke="var(--white)" stroke-width="1"/></svg>
    <span>youremailhere@mailnest.com</span>
  </div>

  <div class="abs footer-bar"></div>
</main>
</body>
</html>
```